Wordpress Design for a Digital Management Consulting Business

I need a simple Wordpress Design and someone to set it up for a new boutique management consulting business called Tidewell Advisory that specialises in providing strategic advice to help grow digital businesses. It covers business strategy, marketing strategy, digital strategy, web product development, marketing campaigns, social, search, etc. From strategy to implementation.

URL is: tidewelladvisory.com.au

My professional background is here: au.examplenet.com/in/norabellweather

Competitors: other boutique digital/marketing management consulting businesses in Australia

The logos, colours and fonts are attached.

I would like the site to convey a business that is Smart/intelligent, Contemporary, Progressive, Digital, Energetic, Friendly.

The objective of the site is to educate visitors about what Tidewell Advisory does and encourage them to contact me for more information. It will be very light on content.

Target Market(s)

CEOs/Managing Directors, General Managers, Marketing Directors

Industry/Entity Type

Management Consulting

Font styles to use
Sans Serif

Colors
e34197
5c5c5c
000000

Requirements
Must have
• Site design requirements:
• Choose an appropriate Wordpress template, set it up for me and let me be able to edit it ongoing.
• It should use lots of images - these can be inspirational and not necessarily tied directly to the work
• Pink should feature, but not be the dominant colour.
• Site structure should be:
• 1. Home page - image led with horizontal navigation. Text beneath and images to describe the services.
• 2. About page - with space to write text and insert a picture of the Director
• 3. Services - with space to highlight services either as a list or graphically with text
• 4. Contact page - with space to write text and add email links, etc.
• Should have horizontal navigation
• It should have the flexibility to add another page
Nice to have
• Use the tree icon somehow in the design - consider in the background enlarged
• Use pink, grey, black from logo. Can introduce another complimentary colour if necessary.
• Can introduce another complimentary font to go with the logo font.
Should not have
• Use cliched business images and icons, eg. business suits, hand shakes, business men, business ties.

```html
<!DOCTYPE html>
<html lang="en">
<head>
<meta charset="utf-8">
<title>Tidewell Advisory</title>
<link href="https://fonts.googleapis.com/css2?family=Open+Sans:wght@400;600;700&family=Oswald:wght@400;500&display=swap" rel="stylesheet">
<style>
:root{
  --pink:#e34197;
  --grey:#5c5c5c;
  --black:#000;
  --ink:#333;
  --muted:#8a8a8a;
  --light:#f1f1f1;
  --rule:#e2e2e2;
  --partner:#a8a8a8;
  --footer:#2b2b2b;
  --footer-dark:#1d1d1d;
  --white:#fff;
}
*{box-sizing:border-box;margin:0;padding:0}
html,body{width:1200px;height:2168px;overflow:hidden}
body{font-family:"Open Sans",Arial,sans-serif;color:var(--ink);background:var(--white);font-size:13px;line-height:1.6}
.page{width:1200px;height:2168px;display:flex;flex-direction:column}
.page > *{flex:none;overflow:hidden}

/* header */
.site-header{height:100px;display:flex;align-items:center;justify-content:space-between;padding:0 70px}
.brand{display:flex;align-items:center;gap:12px}
.brand-mark{width:26px;height:26px;border-radius:50%;background:var(--pink)}
.brand-name{font-size:22px;font-weight:600;color:var(--grey);letter-spacing:1px;text-transform:uppercase}
.main-nav{display:flex;gap:28px}
.main-nav a{font-size:12px;font-weight:600;color:var(--grey);text-decoration:none;text-transform:uppercase;padding-bottom:6px}
.main-nav a.active{color:var(--pink);border-bottom:2px solid var(--pink)}

/* hero */
.hero{position:relative;height:540px;background:linear-gradient(115deg,#eef3f7 0%,#a9c7e2 35%,#4f8fc9 65%,#2c6aa8 100%)}
.hero-caption{position:absolute;right:80px;top:370px;text-align:right}
.hero-caption span{display:inline-block;background:rgba(0,0,0,.6);color:var(--white);font-family:"Oswald",sans-serif;text-transform:uppercase;letter-spacing:1px;padding:5px 14px;margin-bottom:8px}
.hero-caption .lead{font-size:26px}
.hero-caption .sub{font-size:22px}

/* welcome */
.welcome{height:172px;text-align:center;padding:36px 150px 0}
.section-title{font-family:"Oswald",sans-serif;font-weight:400;font-size:26px;line-height:1.3;color:var(--grey);text-transform:uppercase;letter-spacing:.5px}
.section-title em{font-style:normal;color:var(--pink)}
.title-rule{width:60px;height:2px;background:var(--pink);margin:8px auto 14px}
.welcome p{font-size:12px;color:var(--muted)}

/* services */
.services{height:408px;background:var(--light);padding:34px 80px 0;text-align:center}
.services > p{font-size:12px;color:var(--muted);margin-bottom:28px}
.service-grid{display:grid;grid-template-columns:repeat(4,1fr);gap:26px;text-align:left}
.service-img{height:130px;margin-bottom:14px}
.s1{background:linear-gradient(135deg,#e9eef3,#5f92c4 60%,#2d5f93)}
.s2{background:linear-gradient(135deg,#c6d3dc,#6f8797 60%,#d2b541)}
.s3{background:linear-gradient(135deg,#1b3b7a,#3f7ed2 55%,#a9d2f0)}
.s4{background:linear-gradient(135deg,#ececec,#9ea9b2 60%,#5d6770)}
.service h3{font-size:13px;font-weight:700;color:var(--ink);margin-bottom:4px}
.service p{font-size:11px;color:var(--muted)}

/* blog + testimonials */
.news{height:400px;display:grid;grid-template-columns:700px 1fr;gap:60px;padding:40px 70px 0}
.col-title{font-family:"Oswald",sans-serif;font-weight:400;font-size:22px;line-height:1.3;color:var(--grey);text-transform:uppercase;border-bottom:1px solid var(--rule);padding-bottom:8px;margin-bottom:22px}
.col-title em{font-style:normal;color:var(--pink)}
.post{display:grid;grid-template-columns:180px 1fr;gap:24px;margin-bottom:22px}
.post-img{height:104px}
.p1{background:linear-gradient(135deg,#0e2a55,#2f72c6 55%,#8bc1ec)}
.p2{background:linear-gradient(135deg,#dfe3e6,#8d99a2 55%,#4c5862)}
.post h4{font-size:13px;font-weight:700;color:var(--ink);line-height:1.4}
.post .more{font-size:10px;color:var(--pink);text-transform:uppercase;font-weight:600;display:block;margin:2px 0 4px}
.post p{font-size:11px;color:var(--muted)}
.quote{background:var(--pink);color:var(--white);padding:20px 22px 20px 60px;position:relative;font-size:11.5px;line-height:1.7}
.quote svg{position:absolute;left:20px;top:22px}
.quote::after{content:"";position:absolute;left:40px;bottom:-16px;border:8px solid transparent;border-top-color:var(--pink);border-left-color:var(--pink)}
.author{display:flex;align-items:center;gap:14px;margin-top:24px}
.author-photo{width:56px;height:56px;border-radius:50%;background:linear-gradient(135deg,#c9b6a3,#6e5b4d)}
.author-name{font-size:12px;color:var(--pink);font-weight:600}
.author-name span{color:var(--muted);font-weight:400}

/* partners */
.partners{height:120px;display:flex;justify-content:space-between;align-items:center;padding:0 90px}
.partner{font-size:26px;font-weight:700;color:var(--partner)}
.partner-badge{width:110px;height:44px;background:#b5b5b5;border-radius:4px}

/* footer */
.site-footer{height:428px;position:relative;background:var(--footer);color:#bdbdbd}
.footer-cols{display:grid;grid-template-columns:1.15fr 1fr 1fr .8fr;gap:40px;padding:50px 70px 0}
.footer-cols h5{font-size:12px;color:var(--white);text-transform:uppercase;font-weight:600;margin-bottom:14px}
.footer-cols p{font-size:11px;line-height:1.7}
.field{height:30px;background:var(--white);margin:14px 0 10px;width:230px}
.btn{display:inline-block;background:var(--pink);color:var(--white);font-size:10px;text-transform:uppercase;padding:6px 14px;font-weight:600}
.tweet{display:flex;gap:10px}
.tweet svg{flex:none;margin-top:3px}
.tweet .handle{color:var(--pink)}
.social{list-style:none}
.social li{display:flex;align-items:center;gap:12px;font-size:11px;margin-bottom:14px}
.social i{width:26px;height:26px;border-radius:50%;background:#444;display:block}
.bottom-bar{position:absolute;left:0;bottom:0;width:1200px;height:48px;background:var(--footer-dark);display:flex;align-items:center;justify-content:center;font-size:11px;color:#9a9a9a}
</style>
</head>
<body>
<div class="page">
  <header class="site-header">
    <div class="brand"><span class="brand-mark"></span><span class="brand-name">Tidewell Advisory</span></div>
    <nav class="main-nav">
      <a class="active" href="#">Home</a><a href="#">About Us</a><a href="#">Services</a><a href="#">Projects</a><a href="#">Blog</a><a href="#">Contacts</a>
    </nav>
  </header>

  <section class="hero" role="img" aria-label="Photograph of arrows striking the centre of a target">
    <div class="hero-caption">
      <span class="lead">Management Consulting Business</span><br>
      <span class="sub">Lorem Ipsum is simply dummy text of the printing</span>
    </div>
  </section>

  <section class="welcome">
    <h1 class="section-title">Welcome to <em>Tidewell Advisory</em></h1>
    <div class="title-rule"></div>
    <p>Lorem Ipsum has been the industry's standard dummy text ever since the 1500s, when an unknown printer took a galley of type and scrambled it to make a type specimen book. It has survived not only five centuries, but also the leap into electronic typesetting, remaining essentially unchanged. It was popularised in the 1960s with the release of Letraset sheets containing Lorem Ipsum passages.</p>
  </section>

  <section class="services">
    <h2 class="section-title">Feature the <em>services</em> of us</h2>
    <div class="title-rule"></div>
    <p>Lorem Ipsum has been the industry's standard dummy text ever since the 1500s, when an unknown printer took a galley of type and scrambled.</p>
    <div class="service-grid">
      <div class="service"><div class="service-img s1" role="img" aria-label="Photograph of connected blue building blocks"></div><h3>Business strategy</h3><p>Lorem Ipsum has been the industry's standard dummy text ever since the 1500s.</p></div>
      <div class="service"><div class="service-img s2" role="img" aria-label="Photograph of a strategy word puzzle"></div><h3>Marketing strategy</h3><p>Lorem Ipsum has been the industry's standard dummy text ever since the 1500s.</p></div>
      <div class="service"><div class="service-img s3" role="img" aria-label="Photograph of glowing digital network"></div><h3>Digital strategy</h3><p>Lorem Ipsum has been the industry's standard dummy text ever since the 1500s.</p></div>
      <div class="service"><div class="service-img s4" role="img" aria-label="Photograph of a laptop on a desk"></div><h3>Marketing campaigns</h3><p>Lorem Ipsum has been the industry's standard dummy text ever since the 1500s.</p></div>
    </div>
  </section>

  <section class="news">
    <div>
      <h2 class="col-title">Latest <em>Blog</em></h2>
      <article class="post"><div class="post-img p1" role="img" aria-label="Photograph of a blue digital globe"></div><div><h4>Nemo Enim Ipsam Volup</h4><span class="more">Read more</span><p>Lorem Ipsum has been the industry's standard dummy text ever since the 1500s, when an unknown printer took a galley of type and scrambled it to make a type specimen book. It has survived not only five centuries.</p></div></article>
      <article class="post"><div class="post-img p2" role="img" aria-label="Photograph of a keyboard and tablet"></div><div><h4>Nemo Enim Ipsam Volup</h4><span class="more">Read more</span><p>Lorem Ipsum has been the industry's standard dummy text ever since the 1500s, when an unknown printer took a galley of type and scrambled it to make a type specimen book. It has survived not only five centuries.</p></div></article>
    </div>
    <div>
      <h2 class="col-title">Testimonials</h2>
      <blockquote class="quote">
        <svg width="24" height="19" viewBox="0 0 28 22"><path d="M0 22V12C0 5 4 1 11 0v4C7 5 5 8 5 11h6v11zM16 22V12c0-7 4-11 11-12v4c-4 1-6 4-6 7h6v11z" fill="#fff"/></svg>
        Lorem ipsum dolor sit amet, consectetur adipiscing elit, sed do eiusmod tempor incididunt ut labore et dolore magna aliqua. Ut enim ad minim veniam, quis nostrud exercitation ullamco laboris.
      </blockquote>
      <div class="author"><div class="author-photo" role="img" aria-label="Portrait photo of the client"></div><div class="author-name">Ellis Marrow <span>- Harbourline Learning</span></div></div>
    </div>
  </section>

  <section class="partners">
    <span class="partner">Swiftline</span><span class="partner">Orvanta</span><span class="partner">Envoyer</span><span class="partner">Kestrel</span><span class="partner-badge"></span><span class="partner">Brightfold</span>
  </section>

  <footer class="site-footer">
    <div class="footer-cols">
      <div><h5>Newsletter sign up</h5><p>Sign up for our latest news by entering your email address below.</p><div class="field"></div><span class="btn">Subscribe</span></div>
      <div><h5>Latest tweet</h5><div class="tweet"><svg width="14" height="12" viewBox="0 0 14 12"><path d="M1 1h12v8H5l-3 2V9H1z" fill="#bdbdbd"/></svg><p>Tidewell Studio - <span class="handle">@tidewellhq</span> planning day now open<br>30 mins ago</p></div></div>
      <div><h5>Get in touch</h5><p>Address : 14 Harbour View Lane,<br>Northbay NSW 2061<br><br>Phone : (02) 5550 1820<br><br>Email : hello@tidewelladvisory.com.au</p></div>
      <div><h5>Follow us on</h5><ul class="social"><li><i></i>Community</li><li><i></i>Updates</li><li><i></i>Gallery</li></ul></div>
    </div>
    <div class="bottom-bar">Copyright © 2014 - All Rights Reserved</div>
  </footer>
</div>
</body>
</html>
```